REDESIGN MAIN BANNER IMAGE FOR MARKETING WEBSITE

I feel like my main banner image is too busy but I like it but i want to see other options. www.brightlanepromoworks.biz I want a nice professional clean design that goes with current theme of site. Must look professional and show the variety of incentives we offer but not be overwelming.

My business is called Brightlane Promo Works and I provide businesses around the world with marketing incentives that they can use to create exciting promotions and contest and marketing giveaways to help attract more customers.

I provide a variety of different types of incentives such as Vacation Certificates, Dining Vouchers, Hotel Savings Cards, Smart Watches, Etc. that businesses can use in their marketing efforts.

I want my main banner image to reflect the variety of different categories of incentives... that I offer here: https://www.brightlanepromoworks.biz/incentives

We can use images of certificates or images.....I just want the content to be the same:

CONTENT FOR MAIN BANNER IMAGE:
INCREASE LEADS AND SALES OVERNIGHT

CREATE EXCITING MARKETING PROMOTIONS GIVING AWAY SMART DEVICES, VACATION CERTIFICATES, DINING VOUCHERS AND OTHER INCENTIVES TO YOUR CUSTOMERS

GET A FREE SAMPLE PACKAGE FOR A LIMITED TIME ONLY

Target Market(s)

b2b business owners, ceo, president, owner, founder

Industry/Entity Type

Promotional

Requirements
Must have
• Hi guys keep in mind the finished product will have to be 1800x840

Nice to have
• I want a nice professional clean design that goes with current theme of site. Must look professional and show the variety of incentives we offer but not be overwelming.
Should not have

```html
<!DOCTYPE html>
<html lang="en">
<head>
<meta charset="utf-8">
<title>Brightlane Promo Works — Main Banner</title>
<link rel="stylesheet" href="https://fonts.googleapis.com/css2?family=Roboto:wght@300;400;700;900&family=Roboto+Condensed:wght@300;400;700&display=swap">
<style>
:root{
  --brand-blue:#1a6fc4;
  --nav-blue:#1d73c9;
  --nav-blue-dark:#155ea8;
  --login-grey:#4a4d52;
  --call-green:#4bb348;
  --lead-blue:#1f7fe0;
  --sales-green:#3fc63a;
  --hero-dark:#1b1d20;
  --tag-red:#c8202a;
  --cta-blue:#2e7bc4;
  --white:#ffffff;
  --ink:#2b2b2b;
  --muted:#6b6f75;
}
*{margin:0;padding:0;box-sizing:border-box}
html,body{width:1200px;height:600px;overflow:hidden;background:var(--white);font-family:"Roboto",Arial,sans-serif}
.banner{position:relative;width:1200px;height:600px;overflow:hidden}

/* header */
.site-header{position:absolute;top:0;left:0;width:1200px;height:73px;background:var(--nav-blue)}
.brand-panel{position:absolute;top:0;left:0;width:307px;height:73px;background:var(--white);clip-path:polygon(0 0,253px 0,307px 73px,0 73px)}
.brand{position:absolute;left:18px;top:23px;display:flex;align-items:center;gap:8px;color:var(--brand-blue);font-family:"Roboto Condensed",sans-serif;font-weight:700;font-size:20px;white-space:nowrap}
.brand-dot{width:26px;height:26px;border-radius:50%;background:var(--brand-blue)}
.main-nav{position:absolute;left:306px;top:0;height:73px;display:flex;align-items:center}
.main-nav a{color:var(--white);text-decoration:none;font-family:"Roboto Condensed",sans-serif;font-size:13px;padding:0 12px;border-right:1px solid rgba(255,255,255,.25);line-height:22px}
.main-nav a:last-child{border-right:none}
.account{position:absolute;top:0;height:73px;width:62px;display:flex;flex-direction:column;align-items:center;justify-content:center;gap:4px;color:var(--white);font-family:"Roboto Condensed",sans-serif;font-size:11px}
.account.login{left:873px;background:var(--login-grey)}
.account.signup{left:935px;background:var(--nav-blue-dark)}
.call-box{position:absolute;left:997px;top:0;width:203px;height:73px;background:var(--call-green);display:flex;align-items:center;padding-left:10px;gap:10px;color:var(--white);font-family:"Roboto Condensed",sans-serif;font-weight:700;font-size:12.5px;line-height:18px}

/* hero */
.hero-photo{position:absolute;top:73px;left:0;width:1200px;height:330px;background:radial-gradient(ellipse at 52% 35%,#4a3e3c 0%,#2a2628 40%,var(--hero-dark) 80%)}
.hero-rule{position:absolute;top:401px;left:0;width:1200px;height:4px;background:var(--sales-green)}
.headline{position:absolute;top:104px;left:0;width:1200px;text-align:center;color:var(--white);font-family:"Roboto Condensed",sans-serif;font-size:48px;font-weight:400;white-space:nowrap;line-height:56px}
.headline .lead,.headline .sales{color:var(--lead-blue);font-family:"Roboto",sans-serif;font-weight:900}
.headline .overnight{color:var(--sales-green)}
.subhead{position:absolute;top:176px;left:0;width:1200px;text-align:center;color:var(--white);font-family:"Roboto Condensed",sans-serif;font-weight:300;font-size:17px;white-space:nowrap;line-height:20px}

/* incentive showcase */
.incentives{position:absolute;top:232px;left:85px;display:flex;gap:14px}
.incentive{width:160px;height:196px;background:var(--white);border-radius:6px;overflow:hidden;box-shadow:0 4px 12px rgba(0,0,0,.35)}
.incentive-photo{width:160px;height:128px}
.incentive-body{padding:10px 12px}
.incentive-tag{display:inline-block;background:var(--tag-red);color:var(--white);font-family:"Roboto Condensed",sans-serif;font-weight:700;font-size:10px;letter-spacing:.5px;padding:2px 6px;border-radius:2px}
.incentive-name{margin-top:6px;color:var(--ink);font-family:"Roboto Condensed",sans-serif;font-weight:700;font-size:13px;line-height:16px}

/* call to action */
.cta{position:absolute;left:133px;top:484px;width:948px;height:78px;background:var(--cta-blue);border-radius:7px;display:flex;align-items:center;justify-content:center;color:var(--white);font-size:31px;font-weight:300;letter-spacing:1.5px;white-space:nowrap;text-decoration:none}
.cta strong{font-weight:900;margin:0 10px}
</style>
</head>
<body>
<div class="banner">
  <header class="site-header">
    <div class="brand-panel">
      <div class="brand"><span class="brand-dot"></span>Brightlane Promo Works</div>
    </div>
    <nav class="main-nav">
      <a href="#">Home</a><a href="#">The Incentives</a><a href="#">Samples</a><a href="#">Industries</a><a href="#">Testimonials</a><a href="#">Faq</a><a href="#">Contact Us</a>
    </nav>
    <div class="account login">
      <svg width="18" height="18" viewBox="0 0 18 18"><circle cx="9" cy="5" r="4" fill="#fff"/><path d="M1 17c0-5 4-7 8-7s8 2 8 7z" fill="#fff"/></svg>LOGIN
    </div>
    <div class="account signup">
      <svg width="18" height="18" viewBox="0 0 18 18"><circle cx="9" cy="9" r="8" fill="none" stroke="#fff" stroke-width="1.6"/><path d="M9 13V5M5.5 8.5 9 5l3.5 3.5" fill="none" stroke="#fff" stroke-width="1.8"/></svg>SIGN UP
    </div>
    <div class="call-box">
      <svg width="18" height="36" viewBox="0 0 18 36"><rect x="1" y="1" width="16" height="34" rx="3" fill="none" stroke="#fff" stroke-width="2"/><rect x="4" y="5" width="10" height="22" fill="#fff"/><circle cx="9" cy="31" r="1.6" fill="#fff"/></svg>
      <div>CALL US: 1-555-014-2280<br>TEXT US: 1-555-014-2291</div>
    </div>
  </header>

  <div class="hero-photo" role="img" aria-label="Blurred photo of a businessman in a suit and tie"></div>
  <div class="hero-rule"></div>
  <h1 class="headline">INCREASE <span class="lead">LEADS</span> AND <span class="sales">SALES</span> <span class="overnight">OVERNIGHT</span></h1>
  <p class="subhead">CREATE EXCITING MARKETING PROMOTIONS GIVING AWAY SMART DEVICES, VACATION CERTIFICATES, DINING VOUCHERS AND OTHER INCENTIVES TO YOUR CUSTOMERS</p>

  <div class="incentives">
    <article class="incentive">
      <div class="incentive-photo" role="img" aria-label="Beach resort pool with palm trees" style="background:linear-gradient(#6fb2e0,#3f8fb8 55%,#2b7fa0)"></div>
      <div class="incentive-body"><span class="incentive-tag">LUXURY</span><p class="incentive-name">4 Night Mexico Beach Resort Getaway</p></div>
    </article>
    <article class="incentive">
      <div class="incentive-photo" role="img" aria-label="Restaurant dishes and drinks on a table" style="background:linear-gradient(#5a2a22,#8a3a2a 55%,#b4683e)"></div>
      <div class="incentive-body"><span class="incentive-tag">$25 OFF</span><p class="incentive-name">$25 Off At Thousands Of Participating Restaurants</p></div>
    </article>
    <article class="incentive">
      <div class="incentive-photo" role="img" aria-label="Hotel room with bed and lamps" style="background:linear-gradient(#6a3b2a,#9a5a3a 55%,#c9a070)"></div>
      <div class="incentive-body"><span class="incentive-tag">HOTEL STAY</span><p class="incentive-name">A 2 Night Hotel Stay In Your City Of Choice</p></div>
    </article>
    <article class="incentive">
      <div class="incentive-photo" role="img" aria-label="Traveller with luggage in a hotel lobby" style="background:linear-gradient(#2d3a4a,#4a5a6a 55%,#7a7060)"></div>
      <div class="incentive-body"><span class="incentive-tag">$200 OFF</span><p class="incentive-name">$200 Off At Over 400,000 Hotel &amp; Resort Properties</p></div>
    </article>
    <article class="incentive">
      <div class="incentive-photo" role="img" aria-label="Wireless earbuds and a tablet" style="background:linear-gradient(#8a8f96,#b5b9be 55%,#e2e2e2)"></div>
      <div class="incentive-body"><span class="incentive-tag">EARBUDS</span><p class="incentive-name">Premium Wireless Earbuds And Smart Devices</p></div>
    </article>
    <article class="incentive">
      <div class="incentive-photo" role="img" aria-label="Cruise ship on open sea" style="background:linear-gradient(#5aa7e6,#7fbde8 50%,#2c6fa8)"></div>
      <div class="incentive-body"><span class="incentive-tag">LUXURY CRUISE</span><p class="incentive-name">A 4 Night Luxury Cruise Getaway</p></div>
    </article>
  </div>

  <a class="cta" href="#">GET A <strong>FREE SAMPLE PACKAGE</strong> FOR A LIMITED TIME ONLY</a>
</div>
</body>
</html>
```